Ardenwell Building and Property Services needs a business card design

We need a business card design for our building and property services business. We already have a logo we just need a creative design and layout on a business card. Emphasis on clean, modern, professional.
Our client targets are mainly body corporates, building managers, construction managers.
We are a building services company that lean more to structural repair of buildings, through concrete rectification and carbon fibre strengthening.
We also refurbish facades, rendering, painting etc
We target higher end body corporates in prestigious locations, hence why we'd like our cards to reflect professionalism, strength, efficiency

Target Market(s)

body corporates, building managers, construction managers

Industry/Entity Type

Construction

Contact Information for Business Card

Ardenwell is the main word, with 'Building and Property Services' underneath.
Level 17, 82 Harlow Street
MERRIDALE
Melbourne
Vic 3094
T: 9518 2736
Duncan Ferris - Director
dunardenwell@mailbox-example.com

Requirements
Must have
• Stand out on the back of the card- strong/ bold, company logo
• All of the contact details written above
Should not have
• I'd like the card to stand out, especially on the back. Id like the company logo to be prominent, although feel free to be creative around it. But remain clean and professional

```html
<!DOCTYPE html>
<html lang="en">
<head>
<meta charset="utf-8">
<title>Ardenwell Building and Property Services – Business Card</title>
<link rel="stylesheet" href="https://fonts.googleapis.com/css2?family=Arimo:wght@400;700&display=swap">
<style>
  :root {
    --page-bg: #d9d6d0;
    --card-black: #0d0d0e;
    --card-black-soft: #26272a;
    --brand-blue: #2f9ad8;
    --brand-blue-deep: #1d74b3;
    --brand-blue-light: #56b4ea;
    --silver-light: #e6e7e8;
    --silver-mid: #b9bbbe;
    --silver-dark: #8e9195;
    --ink: #111111;
    --contact-text: #ffffff;
  }
  * { box-sizing: border-box; margin: 0; padding: 0; }
  html, body {
    width: 1200px;
    height: 950px;
    overflow: hidden;
    background: var(--page-bg);
  }
  .sheet {
    position: relative;
    width: 1200px;
    height: 950px;
  }
  .card {
    position: absolute;
    left: 232px;
    width: 736px;
    height: 420px;
    overflow: hidden;
    border-radius: 3px;
    box-shadow: 0 10px 26px rgba(0, 0, 0, 0.28);
  }
  .card--back { top: 38px; }
  .card--front { top: 492px; }

  .gloss {
    background:
      linear-gradient(100deg, rgba(255,255,255,0) 62%, rgba(255,255,255,0.10) 74%, rgba(255,255,255,0) 86%),
      linear-gradient(160deg, var(--card-black-soft) 0%, var(--card-black) 45%, #050505 100%);
  }

  /* Company name lockup: plain text in the card's own typeface */
  .brand {
    display: flex;
    flex-direction: column;
    align-items: center;
    text-align: center;
    font-family: "Arimo", sans-serif;
    color: var(--contact-text);
  }
  .brand__row {
    display: flex;
    align-items: center;
    gap: 14px;
  }
  .brand__square {
    width: 20px;
    height: 20px;
    background: var(--brand-blue);
  }
  .brand__name {
    font-weight: 700;
    letter-spacing: 0.04em;
    line-height: 1;
    text-transform: uppercase;
  }
  .brand__tagline {
    font-weight: 700;
    letter-spacing: 0.06em;
    text-transform: uppercase;
    margin-top: 8px;
  }

  .card--back .brand {
    position: absolute;
    left: 0; right: 0;
    top: 168px;
  }
  .card--back .brand__name { font-size: 50px; }
  .card--back .brand__tagline { font-size: 14px; }

  /* Front */
  .front__top {
    position: absolute;
    left: 0; top: 0;
    width: 100%;
    height: 218px;
  }
  .front__top .brand {
    position: absolute;
    left: 150px;
    right: 40px;
    top: 112px;
  }
  .front__top .brand__name { font-size: 34px; }
  .front__top .brand__tagline { font-size: 10px; margin-top: 6px; }
  .front__top .brand__square { width: 14px; height: 14px; gap: 10px; }

  .name-band {
    position: absolute;
    left: 0; top: 218px;
    width: 100%;
    height: 66px;
    background: linear-gradient(180deg, var(--silver-light) 0%, var(--silver-mid) 60%, var(--silver-dark) 100%);
    border-top: 2px solid #f4f4f4;
    text-align: center;
    padding-left: 120px;
    padding-top: 10px;
  }
  .name-band__name {
    font-family: "Arimo", sans-serif;
    font-weight: 700;
    font-size: 27px;
    color: var(--ink);
    letter-spacing: 0.02em;
    text-transform: uppercase;
    line-height: 1.05;
  }
  .name-band__role {
    font-family: "Arimo", sans-serif;
    font-weight: 400;
    font-size: 16px;
    color: var(--ink);
    letter-spacing: 0.06em;
    text-transform: uppercase;
  }

  .contact-band {
    position: absolute;
    left: 0; top: 284px;
    width: 100%;
    height: 136px;
    background: linear-gradient(180deg, var(--brand-blue-light) 0%, var(--brand-blue) 45%, var(--brand-blue-deep) 100%);
    padding: 16px 34px 0 44px;
    font-family: "Arimo", sans-serif;
    font-size: 17px;
    color: var(--contact-text);
  }
  .contact-line {
    display: flex;
    align-items: center;
    gap: 14px;
    height: 28px;
    white-space: nowrap;
  }
  .contact-line--spread {
    justify-content: flex-end;
    padding-right: 8px;
  }
  .contact-item {
    display: inline-flex;
    align-items: center;
    gap: 8px;
  }
  .icon { width: 17px; height: 17px; flex: none; }
</style>
</head>
<body>
<main class="sheet">

  <section class="card card--back gloss" aria-label="Card back">
    <div class="brand">
      <div class="brand__row">
        <span class="brand__square"></span>
        <span class="brand__name">Ardenwell</span>
      </div>
      <span class="brand__tagline">Building and Property Services</span>
    </div>
  </section>

  <section class="card card--front" aria-label="Card front">
    <div class="front__top gloss">
      <div class="brand">
        <div class="brand__row">
          <span class="brand__square"></span>
          <span class="brand__name">Ardenwell</span>
        </div>
        <span class="brand__tagline">Building and Property Services</span>
      </div>
    </div>

    <div class="name-band">
      <p class="name-band__name">Duncan Ferris</p>
      <p class="name-band__role">Director</p>
    </div>

    <div class="contact-band">
      <p class="contact-line">Level 17, 82 Harlow Street, MERRIDALE, Melbourne, Vic 3094</p>
      <p class="contact-line">
        <span class="contact-item">
          <svg class="icon" viewBox="0 0 24 24" aria-hidden="true"><path fill="#fff" d="M6.6 10.8a15.1 15.1 0 0 0 6.6 6.6l2.2-2.2a1 1 0 0 1 1-.25 11.4 11.4 0 0 0 3.6.57 1 1 0 0 1 1 1V20a1 1 0 0 1-1 1A17 17 0 0 1 3 4a1 1 0 0 1 1-1h3.5a1 1 0 0 1 1 1c0 1.25.2 2.45.57 3.57a1 1 0 0 1-.25 1z"/></svg>
          9518 2736
        </span>
        <span class="contact-item">
          <svg class="icon" viewBox="0 0 24 24" aria-hidden="true"><rect x="2" y="5" width="20" height="14" rx="1.5" fill="#fff"/><path d="M3 6.5l9 6.5 9-6.5" fill="none" stroke="#1d74b3" stroke-width="1.6"/></svg>
          dunardenwell@mailbox-example.com
        </span>
      </p>
      <p class="contact-line contact-line--spread">
        <span class="contact-item">
          <svg class="icon" viewBox="0 0 24 24" aria-hidden="true"><circle cx="12" cy="12" r="9.5" fill="none" stroke="#fff" stroke-width="2"/><ellipse cx="12" cy="12" rx="4" ry="9.5" fill="none" stroke="#fff" stroke-width="1.6"/><path d="M2.5 12h19" stroke="#fff" stroke-width="1.6"/></svg>
          www.ardenwell-example.com
        </span>
      </p>
    </div>
  </section>

</main>
</body>
</html>
```